RLT PowerPoint

I am looking for a clean, corporate PowerPoint template.

I would like the following:
- title slide
- break slide
- blank slide with title (for graphs or graphics)
- an ending slide.

Target Market(s)

Business professionals, medium to large business clients.

Requirements
Must have
• Must incorporate the RLT logo in either the header or footer

```html
<!DOCTYPE html>
<html lang="en">
<head>
<meta charset="utf-8">
<title>RLT Slide – Title and Bullets</title>
<link href="https://fonts.googleapis.com/css2?family=Gelasio:wght@700&family=Ubuntu:wght@400;500&display=swap" rel="stylesheet">
<style>
  :root {
    --blue-deep: #2450c0;
    --blue-mid: #3a6ee0;
    --blue-light: #5590f5;
    --rule-dark: #111111;
    --curve-line: #3a2418;
    --text-body: #333333;
    --white: #ffffff;
    --bullet-edge: #1c3f9c;
  }
  * { margin: 0; padding: 0; box-sizing: border-box; }
  html, body {
    width: 1200px;
    height: 900px;
    overflow: hidden;
    background: var(--white);
  }
  .slide {
    position: relative;
    width: 1200px;
    height: 900px;
    overflow: hidden;
    background: var(--white);
    font-family: "Ubuntu", Arial, sans-serif;
  }
  .slide-header {
    position: absolute;
    left: 0; top: 0;
    width: 1200px;
    height: 93px;
    background: linear-gradient(90deg, var(--blue-deep) 0%, var(--blue-mid) 30%, var(--blue-light) 62%, var(--blue-mid) 85%, var(--blue-deep) 100%);
    border-bottom: 3px solid var(--rule-dark);
  }
  .slide-title {
    position: absolute;
    left: 30px; top: 18px;
    font-family: "Gelasio", Georgia, serif;
    font-weight: 700;
    font-size: 44px;
    color: var(--white);
    letter-spacing: 0.3px;
  }
  .header-mark {
    position: absolute;
    right: 12px; top: 8px;
    font-family: "Ubuntu", Arial, sans-serif;
    font-weight: 500;
    font-size: 64px;
    line-height: 1;
    color: rgba(255, 255, 255, 0.16);
  }
  .bullet-list {
    position: absolute;
    left: 33px; top: 177px;
    width: 1060px;
    list-style: none;
  }
  .bullet-item {
    position: relative;
    padding-left: 54px;
    font-size: 22px;
    font-weight: 500;
    line-height: 37.5px;
    color: var(--text-body);
  }
  .bullet-item + .bullet-item { margin-top: 55px; }
  .bullet-icon {
    position: absolute;
    left: 0; top: 3px;
    width: 33px; height: 33px;
  }
  .slide-footer {
    position: absolute;
    left: 0; top: 0;
    width: 1200px; height: 900px;
    pointer-events: none;
  }
  .footer-brand {
    position: absolute;
    left: 20px; top: 830px;
    font-family: "Ubuntu", Arial, sans-serif;
    font-weight: 500;
    font-size: 34px;
    color: var(--white);
    white-space: nowrap;
  }
  .copyright {
    position: absolute;
    left: 898px; top: 853px;
    font-size: 19px;
    color: var(--white);
    letter-spacing: -0.3px;
  }
  .page-number {
    position: absolute;
    left: 1097px; top: 826px;
    width: 58px; height: 58px;
    border: 3px solid var(--white);
    border-radius: 50%;
    display: flex;
    align-items: center;
    justify-content: center;
    font-size: 23px;
    font-weight: 500;
    color: var(--white);
  }
</style>
</head>
<body>
<main class="slide">
  <header class="slide-header">
    <h1 class="slide-title">Project Title here</h1>
    <span class="header-mark" aria-hidden="true">RLT</span>
  </header>

  <ul class="bullet-list">
    <li class="bullet-item">
      <svg class="bullet-icon" viewBox="0 0 33 33" aria-hidden="true">
        <defs>
          <radialGradient id="bulletFill" cx="40%" cy="35%" r="70%">
            <stop offset="0%" stop-color="#6fa0ff"/>
            <stop offset="100%" stop-color="#1d47b8"/>
          </radialGradient>
        </defs>
        <circle cx="16.5" cy="16.5" r="15" fill="url(#bulletFill)" stroke="#1c3f9c" stroke-width="1.5"/>
        <path d="M13 10 L20 16.5 L13 23" fill="none" stroke="#ffffff" stroke-width="3.6" stroke-linecap="round" stroke-linejoin="round"/>
      </svg>
      Lorem ipsum dolor sit ipsum Lorem ipsum dolor sit ipsum Lorem ipsum dolor sit ipsum
    </li>
    <li class="bullet-item">
      <svg class="bullet-icon" viewBox="0 0 33 33" aria-hidden="true">
        <circle cx="16.5" cy="16.5" r="15" fill="url(#bulletFill)" stroke="#1c3f9c" stroke-width="1.5"/>
        <path d="M13 10 L20 16.5 L13 23" fill="none" stroke="#ffffff" stroke-width="3.6" stroke-linecap="round" stroke-linejoin="round"/>
      </svg>
      Lorem ipsum dolor sit ipsum Lorem ipsum dolor sit ipsum Lorem ipsum dolor sit ipsumLorem ipsum dolor sit ipsum Lorem ipsum dolor
    </li>
    <li class="bullet-item">
      <svg class="bullet-icon" viewBox="0 0 33 33" aria-hidden="true">
        <circle cx="16.5" cy="16.5" r="15" fill="url(#bulletFill)" stroke="#1c3f9c" stroke-width="1.5"/>
        <path d="M13 10 L20 16.5 L13 23" fill="none" stroke="#ffffff" stroke-width="3.6" stroke-linecap="round" stroke-linejoin="round"/>
      </svg>
      Lorem Lorem ipsum dolor sit ipsum Lorem ipsum dolor sit ipsum Lorem ipsum dolor sit ipsum Lorem ipsum dolor sit ipsum Lorem ipsum dolor sit ipsum Lorem ipsum dolor sit ipsumipsum dolor sit ipsum Lorem ipsum dolor sit ipsum Lorem ipsum dolor sit ipsum
    </li>
    <li class="bullet-item">
      <svg class="bullet-icon" viewBox="0 0 33 33" aria-hidden="true">
        <circle cx="16.5" cy="16.5" r="15" fill="url(#bulletFill)" stroke="#1c3f9c" stroke-width="1.5"/>
        <path d="M13 10 L20 16.5 L13 23" fill="none" stroke="#ffffff" stroke-width="3.6" stroke-linecap="round" stroke-linejoin="round"/>
      </svg>
      Lorem ipsum dolor sit ipsum Lorem ipsum dolor sit ipsum Lorem ipsum dolor sit ipsumLorem ipsum dolor sit ipsum Lorem ipsum dolor
    </li>
  </ul>

  <footer>
    <svg class="slide-footer" viewBox="0 0 1200 900" aria-hidden="true">
      <defs>
        <linearGradient id="footerFill" x1="0" y1="0" x2="1" y2="0">
          <stop offset="0%" stop-color="#2450c0"/>
          <stop offset="45%" stop-color="#5590f5"/>
          <stop offset="80%" stop-color="#3a6ee0"/>
          <stop offset="100%" stop-color="#2450c0"/>
        </linearGradient>
      </defs>
      <path d="M0 755 C 280 785, 480 862, 690 860 C 900 858, 1090 805, 1200 740 L1200 900 L0 900 Z" fill="url(#footerFill)"/>
      <path d="M0 755 C 280 785, 480 862, 690 860 C 900 858, 1090 805, 1200 740" fill="none" stroke="#3a2418" stroke-width="3"/>
    </svg>
    <div class="footer-brand">RLT Ross Lane Advisory</div>
    <p class="copyright">Copyright text here</p>
    <div class="page-number">01</div>
  </footer>
</main>
</body>
</html>
```